create clean, simple business card template

using the logo created now we need to create a simple, elegant business card design to suit

Industry/Entity Type

Business

Font styles to use
Other font styles liked:
• segoe ui

Requirements
Must have
• Front:
"Name:"
"Title:"
"Mobile:"
"email:"
and the logo

Back:
Logo
Nice to have
• Text in black but other graphics etc to match colours in logo as provided

```html
<!DOCTYPE html>
<html lang="en">
<head>
<meta charset="utf-8">
<title>K&amp;M Estates — Business Card Options</title>
<link rel="stylesheet" href="https://fonts.googleapis.com/css2?family=Cinzel:wght@600&family=Crimson+Text:wght@400;600&family=Arimo:ital@0;1&display=swap">
<style>
  :root{
    --page:#ffffff;
    --card:#ffffff;
    --edge:#1c1c1c;
    --olive:#857327;
    --ink:#111111;
  }
  *{box-sizing:border-box;margin:0;padding:0}
  html,body{width:1200px;height:766px;overflow:hidden;background:var(--page)}
  .sheet{position:relative;width:1200px;height:766px}
  .card{position:absolute;width:292px;height:181px;background:var(--card);border:1.5px solid var(--edge);overflow:hidden}
  .col-1{left:121px}.col-2{left:484px}.col-3{left:845px}
  .row-1{top:61px}.row-2{top:314px}.row-3{top:571px}

  .brand{position:absolute;font-family:"Cinzel",serif;font-weight:600;color:var(--olive);font-size:16px;letter-spacing:.5px;white-space:nowrap;display:flex;align-items:center;gap:8px}
  .brand-dot{width:12px;height:12px;border-radius:50%;background:var(--olive);flex:none}

  .contact{position:absolute;font-family:"Crimson Text",serif;color:var(--ink);display:flex;flex-direction:column;white-space:nowrap}
  .contact .name{font-family:"Cinzel",serif;font-weight:600;color:var(--olive);font-size:16px;line-height:18px}
  .contact .title{font-family:"Crimson Text",serif;font-weight:600;font-size:9.5px;letter-spacing:.3px;text-transform:uppercase;margin-top:2px}
  .contact .phone{font-size:10px;margin-top:9px;line-height:12px}
  .contact .email{font-size:10px;line-height:13px}
  .contact.centered{align-items:center;text-align:center}
  .contact.right{align-items:flex-end;text-align:right}

  .contact.sans,.contact.sans .name,.contact.sans .title{font-family:"Arimo",sans-serif}
  .contact.sans .name{font-weight:400;font-size:15px}
  .contact.sans .title{font-weight:400;text-transform:none;font-size:9.5px;letter-spacing:0;margin-top:4px}
  .contact.sans .phone{margin-top:10px}
  .contact.sans.italic-title .title{font-style:italic}

  .brand.large{font-size:22px}
</style>
</head>
<body>
<main class="sheet">

  <!-- Back, brand centred -->
  <section class="card col-1 row-1">
    <div class="brand" style="left:50%;top:78px;transform:translateX(-50%)"><span class="brand-dot"></span>K&amp;M Estates</div>
  </section>

  <!-- Back, brand with divider -->
  <section class="card col-2 row-1">
    <div class="brand large" style="left:50%;top:74px;transform:translateX(-50%)"><span class="brand-dot"></span>K&amp;M Estates</div>
  </section>

  <!-- Front, centred layout -->
  <section class="card col-3 row-1">
    <div class="brand" style="left:50%;top:34px;transform:translateX(-50%)">K&amp;M Estates</div>
    <div class="contact centered" style="left:0;right:0;top:80px">
      <span class="name">Maria Lestari</span>
      <span class="title">Chief Executive Officer</span>
      <span class="phone">+6281234509876</span>
      <span class="email">maria.lestari@mail.com</span>
    </div>
  </section>

  <!-- Front, brand top-left -->
  <section class="card col-1 row-2">
    <div class="brand" style="left:15px;top:28px">K&amp;M Estates</div>
    <div class="contact" style="left:100px;top:76px">
      <span class="name">Maria Lestari</span>
      <span class="title">Chief Executive Officer</span>
      <span class="phone">+6281234509876</span>
      <span class="email">maria.lestari@mail.com</span>
    </div>
  </section>

  <!-- Front, brand top-right -->
  <section class="card col-2 row-2">
    <div class="brand" style="right:18px;top:24px">K&amp;M Estates</div>
    <div class="contact right" style="right:97px;top:78px">
      <span class="name">Maria Lestari</span>
      <span class="title">Chief Executive Officer</span>
      <span class="phone">+6281234509876</span>
      <span class="email">maria.lestari@mail.com</span>
    </div>
  </section>

  <!-- Front, brand bottom-right -->
  <section class="card col-3 row-2">
    <div class="contact right" style="right:95px;top:48px">
      <span class="name">Maria Lestari</span>
      <span class="title">Chief Executive Officer</span>
      <span class="phone">+6281234509876</span>
      <span class="email">maria.lestari@mail.com</span>
    </div>
    <div class="brand" style="right:14px;bottom:18px">K&amp;M Estates</div>
  </section>

  <!-- Front, large brand bottom-left -->
  <section class="card col-1 row-3">
    <div class="contact right" style="right:20px;top:46px">
      <span class="name">Maria Lestari</span>
      <span class="title">Chief Executive Officer</span>
      <span class="phone">+6281234509876</span>
      <span class="email">maria.lestari@mail.com</span>
    </div>
    <div class="brand large" style="left:12px;bottom:24px"><span class="brand-dot"></span>K&amp;M Estates</div>
  </section>

  <!-- Front, sans-serif -->
  <section class="card col-2 row-3">
    <div class="brand" style="left:15px;top:26px">K&amp;M Estates</div>
    <div class="contact sans" style="left:96px;top:76px">
      <span class="name">Maria Lestari</span>
      <span class="title">Chief Executive Officer</span>
      <span class="phone">+6281234509876</span>
      <span class="email">maria.lestari@mail.com</span>
    </div>
  </section>

  <!-- Front, sans-serif with italic title -->
  <section class="card col-3 row-3">
    <div class="brand" style="left:15px;top:26px">K&amp;M Estates</div>
    <div class="contact sans italic-title" style="left:106px;top:76px">
      <span class="name">Maria Lestari</span>
      <span class="title">Chief Executive Officer</span>
      <span class="phone">+6281234509876</span>
      <span class="email">maria.lestari@mail.com</span>
    </div>
  </section>

</main>
</body>
</html>
```